EYE CATCHING Tralvoni And Website Banner Ads

I am a boutique real-estate agency in Brisbane Australia. I need an eye catching banner ad design for tralvoni and also other website.Color scheme must be the same as logo but must use eye catching text and images to draw people to clickSee brochure ads for inspirationBanner sizes as follows1200x628 pixel (tralvoni)728x90 pixel472x114 pixel300x600 pixel160x600 pixel

Target Market(s)

Home Owners

Industry/Entity Type

Real Estate Agent

Colors

Designer to choose colors to be used in the design.

Requirements
Must have
• It is very important designs must be clear and easy to read
• Each ad MUST have a call to action button "Learn More"
• Color scheme must be the same as logo
• Must be Eye catching
• Must convey trustworthiness and professionalism
• Must be different to all the other real estate ads! A little modern!
Should not have
• Must not be cluttered and too busy

```html
<!DOCTYPE html>
<html lang="en">
<head>
<meta charset="utf-8">
<title>Harbourline Realty – Banner Ads</title>
<link href="https://fonts.googleapis.com/css2?family=Cinzel:wght@500&family=Poppins:wght@500;600&display=swap" rel="stylesheet">
<style>
  :root {
    --navy: #03263f;
    --paper: #ffffff;
    --backdrop: #d9d9d9;
    --ink: #0b1e2e;
  }
  html, body {
    margin: 0;
    width: 1200px;
    height: 1200px;
    overflow: hidden;
    background: var(--backdrop);
  }
  .board {
    position: relative;
    width: 1200px;
    height: 1200px;
  }
  .board__accent {
    position: absolute;
    inset: 0;
  }
  .banner {
    position: absolute;
    left: 120px;
    width: 960px;
    height: 502px;
    filter: drop-shadow(0 4px 8px rgba(0, 0, 0, 0.18));
  }
  .banner--primary { top: 58px; }
  .banner--alternate { top: 640px; }
  .brand-name {
    font-family: "Cinzel", "Times New Roman", serif;
    font-weight: 500;
    fill: var(--navy);
  }
  .headline {
    font-family: "Cinzel", "Times New Roman", serif;
    font-weight: 500;
    font-size: 62px;
    fill: var(--navy);
  }
  .cta-label {
    font-family: "Poppins", Arial, sans-serif;
    font-weight: 600;
    font-size: 22px;
    fill: var(--paper);
  }
  .contact-label {
    font-family: "Poppins", Arial, sans-serif;
    font-weight: 500;
    font-size: 19px;
    fill: var(--ink);
  }
  .contact-phone {
    font-family: "Poppins", Arial, sans-serif;
    font-weight: 500;
    font-size: 46px;
    fill: var(--ink);
  }
  .tile { stroke: var(--paper); stroke-width: 8; }
</style>
</head>
<body>
<div class="board">
  <svg class="board__accent" width="1200" height="1200" viewBox="0 0 1200 1200" aria-hidden="true">
    <polygon points="0,0 720,0 832,60 208,560 0,696" fill="var(--navy)"/>
  </svg>

  <!-- Primary banner: agent portrait on the right -->
  <svg class="banner banner--primary" viewBox="0 0 1200 628">
    <defs>
      <linearGradient id="portraitTone" x1="0" y1="0" x2="0" y2="1">
        <stop offset="0" stop-color="#c9d3c4"/>
        <stop offset="0.55" stop-color="#8a6a54"/>
        <stop offset="1" stop-color="#7a3a1c"/>
      </linearGradient>
      <linearGradient id="interiorTone" x1="0" y1="0" x2="1" y2="1">
        <stop offset="0" stop-color="#f1efea"/>
        <stop offset="1" stop-color="#c9a987"/>
      </linearGradient>
      <linearGradient id="houseTone" x1="0" y1="0" x2="0" y2="1">
        <stop offset="0" stop-color="#3b79d8"/>
        <stop offset="0.35" stop-color="#e3e6ea"/>
        <stop offset="1" stop-color="#6f8f58"/>
      </linearGradient>
      <linearGradient id="gardenTone" x1="0" y1="0" x2="0" y2="1">
        <stop offset="0" stop-color="#5f8fc8"/>
        <stop offset="0.5" stop-color="#5c9a3e"/>
        <stop offset="1" stop-color="#8a5d3b"/>
      </linearGradient>
    </defs>
    <rect width="1200" height="628" fill="var(--paper)"/>

    <g class="brand">
      <text class="brand-name" x="30" y="108" font-size="37">HARBOURLINE</text>
      <text class="brand-name" x="30" y="158" font-size="52">REALTY</text>
    </g>

    <g class="headline-group">
      <text class="headline" x="34" y="290">FULL SERVICE</text>
      <text class="headline" x="32" y="355">COMMISSION</text>
      <text class="headline" x="32" y="420">AGENCY</text>
    </g>

    <g class="cta">
      <rect x="30" y="441" width="227" height="54" rx="7" fill="var(--navy)"/>
      <text class="cta-label" x="143.5" y="476" text-anchor="middle">Learn More</text>
    </g>

    <g class="contact">
      <text class="contact-label" x="279" y="557">Contact Marcus Today:</text>
      <text class="contact-phone" x="280" y="611">0400 123 456</text>
    </g>

    <polygon points="960,0 1200,0 1200,32 1095,137" fill="var(--navy)"/>

    <g class="photo-tiles" role="img" aria-label="Property photos: bright living rooms, a white weatherboard house and a garden deck">
      <polygon class="tile" points="1098,182 1200,80 1200,284" fill="url(#interiorTone)"/>
      <polygon class="tile" points="930,340 1088,182 1200,294 1200,380 1045,455" fill="url(#houseTone)"/>
      <polygon class="tile" points="1090,470 1200,360 1200,580" fill="url(#houseTone)"/>
      <polygon class="tile" points="790,480 945,325 1082,462 927,617" fill="url(#interiorTone)"/>
      <polygon class="tile" points="640,632 770,502 900,632" fill="url(#interiorTone)"/>
      <polygon class="tile" points="930,632 1090,472 1200,582 1200,632" fill="url(#gardenTone)"/>
    </g>

    <g class="portrait">
      <polyline points="568,234 777,25 980,229" fill="none" stroke="var(--navy)" stroke-width="9"/>
      <polygon points="576,238 777,37 972,232 776,449" fill="url(#portraitTone)" role="img" aria-label="Portrait of the agent holding his spaniel"/>
    </g>
  </svg>

  <!-- Alternate banner: agent portrait on the left -->
  <svg class="banner banner--alternate" viewBox="0 0 1200 628">
    <defs>
      <linearGradient id="portraitToneB" x1="0" y1="0" x2="0" y2="1">
        <stop offset="0" stop-color="#c9d3c4"/>
        <stop offset="0.55" stop-color="#8a6a54"/>
        <stop offset="1" stop-color="#7a3a1c"/>
      </linearGradient>
      <linearGradient id="interiorToneB" x1="0" y1="0" x2="1" y2="1">
        <stop offset="0" stop-color="#f1efea"/>
        <stop offset="1" stop-color="#c9a987"/>
      </linearGradient>
      <linearGradient id="houseToneB" x1="0" y1="0" x2="0" y2="1">
        <stop offset="0" stop-color="#3b79d8"/>
        <stop offset="0.35" stop-color="#e3e6ea"/>
        <stop offset="1" stop-color="#6f8f58"/>
      </linearGradient>
      <linearGradient id="gardenToneB" x1="0" y1="0" x2="0" y2="1">
        <stop offset="0" stop-color="#5f8fc8"/>
        <stop offset="0.5" stop-color="#5c9a3e"/>
        <stop offset="1" stop-color="#8a5d3b"/>
      </linearGradient>
    </defs>
    <rect width="1200" height="628" fill="var(--paper)"/>

    <g class="photo-tiles" role="img" aria-label="Property photos: a timber deck and a sunlit interior">
      <polygon class="tile" points="0,360 100,460 0,560" fill="url(#gardenToneB)"/>
      <polygon class="tile" points="0,560 135,470 275,632 0,632" fill="url(#interiorToneB)"/>
    </g>

    <g class="portrait">
      <polyline points="0,143 116,27 320,231" fill="none" stroke="var(--navy)" stroke-width="9"/>
      <polygon points="0,154 116,38 312,234 116,450 0,334" fill="url(#portraitToneB)" role="img" aria-label="Portrait of the agent holding his spaniel"/>
    </g>

    <g class="brand">
      <text class="brand-name" x="296" y="120" font-size="37">HARBOURLINE</text>
      <text class="brand-name" x="296" y="170" font-size="52">REALTY</text>
    </g>

    <g class="headline-group">
      <text class="headline" x="386" y="285">FULL SERVICE</text>
      <text class="headline" x="384" y="350">COMMISSION</text>
      <text class="headline" x="384" y="415">AGENCY</text>
    </g>

    <g class="cta">
      <rect x="382" y="430" width="227" height="54" rx="7" fill="var(--navy)"/>
      <text class="cta-label" x="495.5" y="465" text-anchor="middle">Learn More</text>
    </g>

    <g class="contact">
      <text class="contact-label" x="293" y="557">Contact Marcus Today:</text>
      <text class="contact-phone" x="294" y="611">0400 123 456</text>
    </g>

    <polygon points="960,0 1200,0 1200,32 1095,137" fill="var(--navy)"/>

    <g class="photo-tiles" role="img" aria-label="Property photos: bright living rooms, a white weatherboard house and a garden deck">
      <polygon class="tile" points="1098,182 1200,80 1200,284" fill="url(#interiorToneB)"/>
      <polygon class="tile" points="930,340 1088,182 1200,294 1200,380 1045,455" fill="url(#houseToneB)"/>
      <polygon class="tile" points="1090,470 1200,360 1200,580" fill="url(#houseToneB)"/>
      <polygon class="tile" points="790,480 945,325 1082,462 927,617" fill="url(#interiorToneB)"/>
      <polygon class="tile" points="640,632 770,502 900,632" fill="url(#interiorToneB)"/>
      <polygon class="tile" points="930,632 1090,472 1200,582 1200,632" fill="url(#gardenToneB)"/>
    </g>
  </svg>
</div>
</body>
</html>
```